Banner Ad for Resume Services Website

The add is for this web site: www.BrightCareerPages.net

The site offers 4 different services:

- Resume Writing (by a Certified Professional Resume Writer)
- Resume Posting (posts your resume to 85 job sites)
- Resume Distribution (sends your resume to hundreds of recruiters)
- Resume Online website (created an online resume with a domain name to your name)

Colors to be used are Blue, Yellow, etc... please check the website for inspiration.

Check the web site to learn more.

Target Market(s)

Unemployed, Professionals who want to switch jobs, etc..

Industry/Entity Type

Requirements
Must have
• We definitely one this to be included on the banner:

"Free Resume Samples"

in order to attract clicks.
Nice to have
• Some of the words we suggest to include on the banner are:

"How Good is Your Resume? Ask a Professional !"

Should not have
• No animation !

Do not place the LOGO on the banner as our LOGO might change in the near future. If you already submitted a banner with the LOGO on it, you can replace it with any other graphic that has a Resume/Jobs/BusinessStaff related theme.

```html
<!DOCTYPE html>
<html lang="en">
<head>
<meta charset="utf-8">
<title>Free Resume Samples – Banner Variations</title>
<link rel="stylesheet" href="https://fonts.googleapis.com/css2?family=Cinzel:wght@700&family=Oswald:wght@700&family=Open+Sans:wght@400;700&display=swap">
<style>
  :root{
    --board-dark:#272826;
    --board-edge:#4a4b48;
    --numeral:#ffffff;
    --banner-white:#ffffff;
    --orange:#f86c12;
    --orange-deep:#e85a06;
    --blue-light:#3a7bcf;
    --blue-dark:#15469a;
    --text-light:#ffffff;
    --text-dark:#111111;
    --lime-top:#d8ff5a;
    --lime-bottom:#8fdc12;
    --lime-edge:#5ea80a;
    --amber-top:#ffc47a;
    --amber-bottom:#f7861c;
    --amber-edge:#c8630c;
    --gold-top:#fff4a0;
    --gold-bottom:#f2d22a;
    --gold-edge:#c6a814;
    --photo-skin:#e9c9b2;
    --photo-paper:#eef0f3;
  }
  *{box-sizing:border-box;margin:0;padding:0}
  html,body{width:1200px;height:621px;overflow:hidden;background:var(--board-dark)}
  .board{
    position:relative;width:1200px;height:621px;
    background:radial-gradient(ellipse at 50% 45%, #3a3b39 0%, var(--board-dark) 75%);
    box-shadow:inset 0 0 0 14px var(--board-edge), inset 0 0 40px 20px rgba(0,0,0,.6);
  }
  .variant{position:absolute;left:0;width:1200px;height:123px}
  .variant--one{top:102px}
  .variant--two{top:256px}
  .variant--three{top:398px}
  .variant__number{
    position:absolute;left:18px;width:70px;top:0;height:123px;
    display:flex;align-items:center;justify-content:center;
    font-family:"Cinzel",serif;font-weight:700;font-size:78px;color:var(--numeral);
  }
  .banner{
    position:absolute;left:123px;top:0;width:1004px;height:123px;
    background:var(--banner-white);border:3px solid var(--banner-white);overflow:hidden;
  }
  .banner__photo{
    position:absolute;left:0;top:0;width:300px;height:117px;
    background:linear-gradient(90deg,var(--photo-skin) 0%,#d9b6a0 30%,var(--photo-paper) 45%,#dfe3e8 100%);
  }
  .banner__panel{
    position:absolute;left:560px;top:0;right:0;height:117px;
    background:linear-gradient(180deg,var(--blue-light) 0%,var(--blue-dark) 100%);
  }
  .banner__arrow{position:absolute;left:0;top:0;width:1000px;height:117px}
  .banner__offer{
    position:absolute;left:262px;width:320px;top:0;height:117px;
    text-align:center;color:var(--text-light);
  }
  .banner__offer-free{
    display:block;font-family:"Oswald",sans-serif;font-weight:700;font-size:62px;line-height:1;margin-top:4px;
  }
  .banner__offer-label{
    display:block;font-family:"Open Sans",sans-serif;font-size:29px;line-height:1;margin-top:4px;
  }
  .banner__pitch{
    position:absolute;left:640px;width:340px;top:12px;text-align:center;
    font-family:"Open Sans",sans-serif;font-size:25px;color:var(--text-light);letter-spacing:-.3px;
  }
  .cta{
    position:absolute;left:676px;top:58px;width:265px;height:42px;
    display:flex;align-items:center;justify-content:center;
    font-family:"Open Sans",sans-serif;font-weight:700;font-size:21px;color:var(--text-dark);letter-spacing:-.4px;
  }
  .cta--lime{
    background:linear-gradient(180deg,var(--lime-top),var(--lime-bottom));
    border:2px solid var(--lime-edge);border-radius:3px;
    box-shadow:0 0 0 2px rgba(200,255,80,.5);
  }
  .cta--amber{
    background:linear-gradient(180deg,var(--amber-top),var(--amber-bottom));
    border:2px solid var(--amber-edge);border-radius:21px;
    box-shadow:inset 0 2px 0 rgba(255,255,255,.5),0 2px 3px rgba(0,0,0,.35);
  }
  .cta--gold{
    background:linear-gradient(180deg,var(--gold-top),var(--gold-bottom));
    border:2px solid var(--gold-edge);border-radius:21px;
    box-shadow:inset 0 2px 0 rgba(255,255,255,.6),0 2px 3px rgba(0,0,0,.35);
  }
</style>
</head>
<body>
<main class="board">

  <section class="variant variant--one">
    <div class="variant__number">1</div>
    <div class="banner">
      <div class="banner__photo" role="img" aria-label="Smiling professional woman with glasses beside a sample resume sheet"></div>
      <div class="banner__panel"></div>
      <svg class="banner__arrow" viewBox="0 0 1000 117" aria-hidden="true">
        <polygon points="222,58.5 270,3 590,3 632,58.5 590,114 270,114" fill="var(--orange)" stroke="var(--banner-white)" stroke-width="4"/>
      </svg>
      <div class="banner__offer"><span class="banner__offer-free">Free</span><span class="banner__offer-label">Resum Samples</span></div>
      <p class="banner__pitch">How Good is Your Resume?</p>
      <a class="cta cta--lime">Ask a Professional !</a>
    </div>
  </section>

  <section class="variant variant--two">
    <div class="variant__number">2</div>
    <div class="banner">
      <div class="banner__photo" role="img" aria-label="Smiling professional woman with glasses beside a sample resume sheet"></div>
      <div class="banner__panel"></div>
      <svg class="banner__arrow" viewBox="0 0 1000 117" aria-hidden="true">
        <polygon points="222,58.5 270,3 590,3 632,58.5 590,114 270,114" fill="var(--orange-deep)" stroke="var(--banner-white)" stroke-width="4"/>
      </svg>
      <div class="banner__offer"><span class="banner__offer-free">Free</span><span class="banner__offer-label">Resum Samples</span></div>
      <p class="banner__pitch">How Good is Your Resume?</p>
      <a class="cta cta--amber">Ask a Professional !</a>
    </div>
  </section>

  <section class="variant variant--three">
    <div class="variant__number">3</div>
    <div class="banner">
      <div class="banner__photo" role="img" aria-label="Smiling professional woman with glasses beside a sample resume sheet"></div>
      <div class="banner__panel"></div>
      <svg class="banner__arrow" viewBox="0 0 1000 117" aria-hidden="true">
        <polygon points="222,58.5 270,3 590,3 632,58.5 590,114 270,114" fill="var(--orange)" stroke="var(--banner-white)" stroke-width="4"/>
      </svg>
      <div class="banner__offer"><span class="banner__offer-free">Free</span><span class="banner__offer-label">Resum Samples</span></div>
      <p class="banner__pitch">How Good is Your Resume?</p>
      <a class="cta cta--gold">Ask a Professional !</a>
    </div>
  </section>

</main>
</body>
</html>
```